Invitation For Service Management Event

We need an invitation for clients to an event on the platform service Management. This has to be appealing and needs to be "tech" inspired. it is important that the design of the invitation is as clean as possible. I attached some images so that you understand the kind of enviorment we want to portray in the invitation.
- I also attached our company logo to the brief under the file Brelunox Transparent. The logo has to be in the invitation.

```html
<!DOCTYPE html>
<html lang="es">
<head>
<meta charset="utf-8">
<title>Platform Service Management – Invitación</title>
<link rel="stylesheet" href="https://fonts.googleapis.com/css2?family=Montserrat:wght@300;400;500;600;700&display=swap">
<style>
  :root {
    --paper: #ffffff;
    --panel: #f4f4f4;
    --night: #05080d;
    --night-mid: #0c2233;
    --glow: #7fd3f2;
    --ink: #111111;
    --ink-soft: #333333;
    --brand-red: #d8232a;
    --mark: #222222;
  }
  * { margin: 0; padding: 0; box-sizing: border-box; }
  html, body { width: 857px; height: 1200px; overflow: hidden; background: var(--paper); }
  body { font-family: "Montserrat", sans-serif; color: var(--ink); }

  .sheet { position: relative; width: 857px; height: 1200px; background: var(--paper); }
  .crop-marks { position: absolute; inset: 0; }

  .hero {
    position: absolute; left: 44px; top: 96px; width: 776px; height: 508px;
    background: var(--night); overflow: hidden;
  }
  .hero-backdrop {
    position: absolute; inset: 0;
    background:
      radial-gradient(ellipse 22% 32% at 50% 50%, rgba(3,6,10,0.9), transparent 100%),
      radial-gradient(ellipse 70% 60% at 50% 50%, rgba(40,120,170,0.45), transparent 75%),
      linear-gradient(180deg, #03060a 0%, var(--night-mid) 50%, #03060a 100%);
  }
  .hero-title {
    position: absolute; left: 0; right: 0; top: 170px; text-align: center; color: #fff;
  }
  .hero-kicker { font-size: 15px; font-weight: 400; letter-spacing: 0.3px; margin-bottom: 14px; }
  .hero-heading {
    font-size: 35px; font-weight: 300; line-height: 1.05; letter-spacing: 1px;
    text-transform: uppercase; color: var(--glow);
  }

  .details {
    position: absolute; left: 44px; top: 604px; width: 776px; height: 476px;
    background: var(--panel); text-align: center;
  }
  .brand {
    position: absolute; top: 64px; left: 0; right: 0;
    display: flex; justify-content: center; align-items: center; gap: 12px;
  }
  .brand-dot { width: 34px; height: 34px; border-radius: 50%; background: var(--brand-red); }
  .brand-name { font-size: 34px; font-weight: 700; color: var(--mark); letter-spacing: 0.5px; }

  .event-date {
    position: absolute; top: 162px; left: 0; right: 0;
    font-size: 23px; font-weight: 600; line-height: 1.3;
  }
  .event-venue { position: absolute; top: 276px; left: 0; right: 0; font-size: 14px; color: var(--ink-soft); }
  .rsvp { position: absolute; top: 352px; left: 0; right: 0; font-size: 14.5px; line-height: 1.4; color: var(--ink-soft); }
  .rsvp strong { color: var(--ink); font-weight: 700; }

  .footer-band { position: absolute; left: 44px; top: 1080px; width: 776px; height: 12px; background: var(--night); }
</style>
</head>
<body>
<main class="sheet">
  <svg class="crop-marks" width="857" height="1200" aria-hidden="true">
    <g stroke="#555" stroke-width="1">
      <line x1="44" y1="0" x2="44" y2="72"/><line x1="0" y1="96" x2="22" y2="96"/>
      <line x1="820" y1="0" x2="820" y2="72"/><line x1="835" y1="96" x2="857" y2="96"/>
      <line x1="44" y1="1116" x2="44" y2="1200"/><line x1="0" y1="1092" x2="22" y2="1092"/>
      <line x1="820" y1="1116" x2="820" y2="1200"/><line x1="835" y1="1092" x2="857" y2="1092"/>
    </g>
  </svg>

  <section class="hero">
    <div class="hero-backdrop" role="img" aria-label="Dark blue technology backdrop with glowing circuit lines, a hexagon grid and a ring emblem framing the title"></div>
    <div class="hero-title">
      <p class="hero-kicker">Come and join us</p>
      <h1 class="hero-heading">Platform<br>Service<br>Management</h1>
    </div>
  </section>

  <section class="details">
    <div class="brand">
      <span class="brand-dot"></span>
      <span class="brand-name">BRELUNOX</span>
    </div>
    <p class="event-date">Jueves, 26 de Noviembre de 2020<br>De 7:00 PM a 9:00 PM</p>
    <p class="event-venue">A través de la plataforma NEXMEET</p>
    <p class="rsvp">
      <strong>RSVP</strong><br>
      Favor enviar confirmación a<br>
      <strong>r.almonte@brelunox.com.do</strong><br>
      o llamando al<br>
      <strong>(809)-555-0142</strong>
    </p>
  </section>

  <div class="footer-band"></div>
</main>
</body>
</html>
```